Institutional website for an IT Consulting company

Web design + HTML + CSS / Bootstrap + JS (interaction) integration in order to extend our existing website brightvale.coop.
Our website is currently aiming only for recruitment and not for customers, we want to provide a fluid transition between customer side website (this project) and recruitment website (existing site).

Ideally we would love the new design to be "inspired" by our actual graphic chart (Colors mainly). It should provide a great user experience and a landing page (or any mean) allowing the visitor to easily switch from the end customer front end (this project), the recruitment front end (existing front end https://www.brightvale.coop/) and the existing member front end (an other existing front end dedicated to members already existing).

In attachment you will find the expected site content mainly a one page with a first level of information and "link" to sub pages (a way to directly access this sub pages should also be provided).

The website should be accessible on mobile device and desktop.

The attachment is in french as it reflect the final site content, but if google translate isn't sufficient to have a general idea of the content, feel free to ask. We would love to have some visual representation for some categories.

Target Market(s)

fortune 500 companies

Industry/Entity Type

It Company

Coding

Coded - Design and coding required

Number of Pages Required

5+ page

Requirements
Must have
• This project must have an easy way to navigate between 3 sub sites, the customer one (the one designed here), the consultant / recruitment one (the existing one at brightvale.coop), the members one.

A one page experience at first leading to detail pages.

Custom made visuals to illustrate each categories.

Inspiration websites : quorb[.]fr ; tasknest[.]com ; dovrally[.] com ...

Be inspired by the existing color from our logo and existing website at brightvale[.]coop

```html
<!DOCTYPE html>
<html lang="en">
<head>
<meta charset="utf-8">
<title>Brightvale.coop – IT Consulting</title>
<link href="https://fonts.googleapis.com/css2?family=Dosis:wght@500;600;700&family=Lato:ital,wght@0,400;0,700;1,400&display=swap" rel="stylesheet">
<style>
:root{
  --teal:#1ba7b0;
  --teal-dark:#0f3f42;
  --teal-deep:#0a2e31;
  --ink:#1d2a2c;
  --text:#6b7677;
  --muted:#9aa3a4;
  --line:#dfe4e5;
  --soft:#f3f5f6;
  --white:#ffffff;
}
*{box-sizing:border-box;margin:0;padding:0}
html,body{width:1200px;height:3696px;overflow:hidden;background:var(--white)}
body{font-family:'Lato',sans-serif;color:var(--text);position:relative}
.abs{position:absolute}
h1,h2,h3,h4{font-family:'Dosis',sans-serif;color:var(--ink);font-weight:600}
.section-title{font-size:28px;display:flex;align-items:center;gap:14px}
.section-title::after{content:"";width:44px;height:3px;background:var(--teal)}
.section-title.light{color:var(--white)}
.section-title.light::after{background:var(--white)}

/* header + hero */
.top{position:absolute;left:0;top:0;width:1200px;height:567px;background:var(--soft)}
.header{position:absolute;left:0;top:0;width:1200px;height:70px;background:var(--white)}
.logo{position:absolute;left:111px;top:16px;font-family:'Dosis',sans-serif;font-weight:700;font-size:26px;color:var(--teal-dark);letter-spacing:1px;display:flex;align-items:center;gap:8px}
.logo .dot{width:12px;height:12px;background:var(--teal)}
.nav-switch{position:absolute;right:113px;top:20px;display:flex;gap:10px}
.nav-switch a{font-size:13px;color:var(--ink);text-decoration:none;padding:7px 12px;border:1px solid var(--line)}
.nav-switch a.plain{border-color:transparent}
.hero-photo{left:111px;top:99px;width:727px;height:436px;background:linear-gradient(120deg,#1f2a2d 0%,#3d4a4c 45%,#7b8a8c 75%,#c9d1d2 100%)}
.search{left:153px;top:303px;width:616px;height:42px;background:var(--white);display:flex;align-items:center;font-size:13px;color:var(--muted)}
.search span{flex:1;padding-left:16px;border-right:1px solid var(--line);display:flex;align-items:center;gap:8px}
.search b{background:var(--teal-dark);color:var(--white);font-weight:700;height:32px;margin:0 5px;padding:0 18px;display:flex;align-items:center}
.hero-copy{left:862px;top:108px;width:230px}
.hero-copy h1{font-size:34px;line-height:38px;font-weight:700;text-transform:uppercase;color:var(--teal-deep)}
.hero-copy p{margin-top:18px;font-size:19px;line-height:30px}

/* provider */
.provider{top:616px;left:111px;width:976px}
.provider p{font-size:14px;line-height:19px;margin-top:4px}
.provider p a{color:var(--ink)}
.skills{left:111px;top:838px;width:740px;display:grid;grid-template-columns:251px 249px 240px;row-gap:24px}
.skill{display:flex;align-items:center;gap:16px;font-size:13px;color:var(--ink);line-height:17px;height:44px}
.focus-box{left:865px;top:845px;width:222px;height:104px;background:var(--soft);border:1px solid var(--line);padding:14px 18px;font-size:12px;line-height:16px}
.focus-box ul{list-style:none;display:flex;gap:24px;margin-top:16px;color:var(--ink)}
.focus-box li::before{content:"› ";color:var(--teal)}
.btn{display:inline-flex;align-items:center;gap:8px;font-size:13px;font-weight:700;padding:0 12px;height:34px;border:1px solid var(--teal-dark);color:var(--teal-dark);background:var(--white);text-decoration:none}
.btn.solid{background:var(--teal-dark);color:var(--white)}
.btn::after{content:"»"}
.provider-actions{left:111px;top:990px;display:flex;gap:8px}

/* why */
.why{left:0;top:1087px;width:1200px;height:493px;background:var(--teal)}
.why .section-title{position:absolute;left:111px;top:48px}
.why-card{top:115px;width:308px;height:311px;background:var(--white);border:3px solid var(--teal-dark);padding:36px 33px}
.why-card h3{font-size:19px;margin-top:18px}
.why-card p{font-size:12px;line-height:18px;margin-top:8px;height:56px}
.why-card .btn{margin-top:22px}
.card-icon{width:44px;height:44px;border-radius:50%;background:#cfeff1}

/* experts */
.experts{left:111px;top:1640px}
.experts-text{left:111px;top:1700px;width:470px;font-size:12.5px;line-height:20px}
.expert-circle{width:148px;height:148px;border-radius:50%;border:5px solid var(--teal);background:linear-gradient(160deg,#e9f7f8,#bfe5e8)}
.expert-label{width:180px;text-align:center;font-family:'Dosis',sans-serif;font-weight:600;font-size:14px;color:var(--ink)}
.strip{left:111px;top:1924px;width:976px;height:136px;background:var(--soft);display:grid;grid-template-columns:repeat(4,1fr)}
.strip div{display:flex;align-items:center;gap:18px;padding-left:24px;font-size:14px;color:var(--ink);border-right:1px solid var(--line)}
.strip div:last-child{border-right:0}
.strip i{width:40px;height:40px;border:2px solid var(--teal);border-radius:4px;flex:none}
.divider{left:0;top:2220px;width:1200px;height:5px;background:linear-gradient(90deg,var(--teal-dark) 0 50%,var(--teal) 50% 100%)}

/* news */
.news-card{top:2358px;width:238px;height:377px;background:linear-gradient(180deg,#2c3a33 0%,#4a5a4c 45%,#1a1f1e 78%,#0c0e0e 100%);display:flex;align-items:flex-end;padding:0 18px 24px}
.news-card h4{color:var(--white);font-family:'Lato',sans-serif;font-weight:700;font-size:15px;line-height:20px}

/* testimonials */
.testimonials{left:0;top:2797px;width:1200px;height:547px;background:linear-gradient(120deg,var(--teal-deep) 0%,#124d50 60%,#0e4346 100%)}
.quote-card{left:190px;top:61px;width:411px;height:422px;background:var(--white);padding:140px 44px 0}
.avatar{left:331px;top:22px;width:132px;height:132px;border-radius:50%;background:linear-gradient(160deg,#9aa5a6,#4b5556);border:3px solid var(--white)}
.quote-card p{font-style:italic;font-size:14px;line-height:22px}
.quote-card h4{font-family:'Lato',sans-serif;font-size:15px;margin-top:18px}
.quote-card em{font-size:12px;color:var(--ink)}
.quote-mark{right:160px;bottom:60px;font-family:'Dosis',sans-serif;font-size:70px;color:#bde6e9;line-height:1}
.say{left:697px;top:85px;width:390px;color:var(--white)}
.say h2{color:var(--white);font-size:28px}
.say p{font-size:12px;line-height:18px;margin-top:14px}
.dots{left:717px;top:280px;display:flex;gap:7px}
.dots span{width:6px;height:6px;border-radius:50%;background:rgba(255,255,255,.5)}
.dots span:first-child{width:9px;height:9px;background:var(--white);margin-top:-1px}
.arrows{left:717px;top:357px;width:148px;height:66px;background:var(--white);display:flex;align-items:center;justify-content:space-around}

/* footer */
.footer{left:0;top:3344px;width:1200px;height:352px}
.footer h4{font-size:16px;text-transform:uppercase;letter-spacing:.5px}
.foot-col{top:48px;font-size:12px;line-height:18px}
.foot-col ul{list-style:none;margin-top:14px}
.foot-col li{line-height:36px}
.foot-col li::before{content:"› ";color:var(--teal)}
.socials{display:flex;gap:14px;margin-top:16px}
.socials span{width:34px;height:34px;border-radius:50%;border:1px solid var(--ink)}
.socials span:first-child{background:var(--teal-dark);border-color:var(--teal-dark)}
.contact-line{display:flex;gap:10px;margin-top:10px}
.newsletter input{margin-top:16px;width:236px;height:32px;border:1px solid var(--line);border-radius:16px;padding:0 14px;font:12px 'Lato',sans-serif}
.newsletter button{display:block;margin-top:12px;background:var(--teal-dark);color:var(--white);border:0;border-radius:16px;height:30px;padding:0 22px;font:700 11px 'Lato',sans-serif}
.copyright{left:0;top:3647px;width:1200px;border-top:1px solid var(--line);text-align:center;padding-top:16px;font-size:11px;color:var(--ink)}
</style>
</head>
<body>

<div class="top">
  <header class="header">
    <div class="logo"><span class="dot"></span>BRIGHTVALE.coop</div>
    <nav class="nav-switch"><a href="#">I am Brightvale</a><a class="plain" href="#">I want to join Brightvale</a></nav>
  </header>
  <div class="abs hero-photo" role="img" aria-label="Photo of a consultant working on a laptop in a bright office"></div>
  <div class="abs search">
    <span><svg width="12" height="12" viewBox="0 0 12 12"><circle cx="5" cy="5" r="4" fill="none" stroke="#9aa3a4" stroke-width="1.5"/><line x1="8" y1="8" x2="11" y2="11" stroke="#9aa3a4" stroke-width="1.5"/></svg>Search</span>
    <span><svg width="10" height="13" viewBox="0 0 10 13"><path d="M5 0a5 5 0 0 1 5 5c0 3.5-5 8-5 8S0 8.5 0 5a5 5 0 0 1 5-5z" fill="#9aa3a4"/></svg>Country, Region, City...</span>
    <b>Search</b>
  </div>
  <div class="abs hero-copy">
    <h1>Brightvale.coop is a services sampans with strong values of cooperation.</h1>
    <p>Ut enim ad minim veniam, quis nostrud exercitation ullamco</p>
  </div>
</div>

<section class="abs provider">
  <h2 class="section-title">Brightvale, a service provider</h2>
  <p style="margin-top:14px">Brightvale.coop is a services sampans with strong values of cooperation , based in particular on an atypical management (<a href="#">Link to Fairshare Scop</a>).<br>
  We have independent profiles on subjects such Nimbra BI, infrastructure and security, Data Platform (<a href="#">Link to Search page</a>).<br>
  But why should you chose only one consultant when brightvale.coop can suggest a whole community to your service?<br>
  Brightvale is first and foremost a team of experts (<a href="#">hyperlink to page "experts in their domain"</a>) including also a few MVPs in cooperation with the group of consultants on a daily basis.</p>
  <p style="margin-top:10px">For example, we can intervene on the following subjects</p>
</section>

<div class="abs skills">
  <div class="skill"><svg width="30" height="34" viewBox="0 0 30 34"><path d="M15 1 28 6v10c0 8-6 14-13 17C8 30 2 24 2 16V6z" fill="none" stroke="#0f3f42" stroke-width="2.5"/><path d="m9 17 4 4 8-8" fill="none" stroke="#1ba7b0" stroke-width="2.5"/></svg>Hybrid architecture</div>
  <div class="skill"><svg width="30" height="34" viewBox="0 0 30 34"><path d="M15 1 28 6v10c0 8-6 14-13 17C8 30 2 24 2 16V6z" fill="none" stroke="#0f3f42" stroke-width="2.5"/><path d="m9 17 4 4 8-8" fill="none" stroke="#1ba7b0" stroke-width="2.5"/></svg>Security and Infrastructure</div>
  <div class="skill"><svg width="30" height="34" viewBox="0 0 30 34"><path d="M15 1 28 6v10c0 8-6 14-13 17C8 30 2 24 2 16V6z" fill="none" stroke="#0f3f42" stroke-width="2.5"/><path d="m9 17 4 4 8-8" fill="none" stroke="#1ba7b0" stroke-width="2.5"/></svg>Expertise on Modern Data Warehouse</div>
  <div class="skill"><svg width="30" height="34" viewBox="0 0 30 34"><path d="M15 1 28 6v10c0 8-6 14-13 17C8 30 2 24 2 16V6z" fill="none" stroke="#0f3f42" stroke-width="2.5"/><path d="m9 17 4 4 8-8" fill="none" stroke="#1ba7b0" stroke-width="2.5"/></svg>Advanced display, especially via VizDeck</div>
  <div class="skill"><svg width="30" height="34" viewBox="0 0 30 34"><path d="M15 1 28 6v10c0 8-6 14-13 17C8 30 2 24 2 16V6z" fill="none" stroke="#0f3f42" stroke-width="2.5"/><path d="m9 17 4 4 8-8" fill="none" stroke="#1ba7b0" stroke-width="2.5"/></svg>Cost rationalisation on Nimbra</div>
  <div class="skill"><svg width="30" height="34" viewBox="0 0 30 34"><path d="M15 1 28 6v10c0 8-6 14-13 17C8 30 2 24 2 16V6z" fill="none" stroke="#0f3f42" stroke-width="2.5"/><path d="m9 17 4 4 8-8" fill="none" stroke="#1ba7b0" stroke-width="2.5"/></svg>Training...</div>
</div>
<aside class="abs focus-box">Our teams are highly oriented on Nimbra topics
  <ul><li>Data Platform</li><li>Data &amp; BI</li></ul>
</aside>
<div class="abs provider-actions">
  <a class="btn solid" href="#">You wish for a quotation</a>
  <a class="btn" href="#">More information?</a>
  <a class="btn" href="#">Contact Us</a>
</div>

<section class="abs why">
  <h2 class="section-title light">Why use a AEC-COPA?</h2>
  <article class="abs why-card" style="left:111px">
    <div class="card-icon" role="img" aria-label="Icon of a consultant"></div>
    <h3>Custom-made S/E</h3>
    <p>Accordingly to your needs, our consultant will be able to assist you in achieving your projects.</p>
    <a class="btn solid" href="#">Find Out More</a>
  </article>
  <article class="abs why-card" style="left:446px">
    <div class="card-icon" role="img" aria-label="Icon of a team"></div>
    <h3>A team at your service</h3>
    <p>Brightvale as a AEC-COPA offers you a service, not from an independent to a customer perspective but from a community to a customer.</p>
    <a class="btn" href="#">Find Out More</a>
  </article>
  <article class="abs why-card" style="left:781px">
    <div class="card-icon" role="img" aria-label="Icon of a handshake"></div>
    <h3>A fair pay</h3>
    <p>At Brightvale, the S/E gain directly what they work for.</p>
    <a class="btn" href="#">Find Out More</a>
  </article>
</section>

<h2 class="abs section-title experts">Experts in their field</h2>
<div class="abs experts-text">
  <p>S/E experts are able to assist you on each standard phase of a data platform project. We also offer formal or custom training but also the capacity of purchasing Nimbra credits or OfficeSuite licences.</p>
  <p style="margin-top:20px">In order to find and directly contact the profile(s) that is/are best suited to your needs, please use our research tool. The customer relationship team is also available to answer to all you inquiries. @</p>
</div>
<div class="abs expert-circle" style="left:606px;top:1663px" role="img" aria-label="Illustration of a data platform project"></div>
<div class="abs expert-circle" style="left:786px;top:1663px" role="img" aria-label="Illustration of training"></div>
<div class="abs expert-circle" style="left:963px;top:1663px" role="img" aria-label="Illustration of a cloud solution provider"></div>
<div class="abs expert-label" style="left:590px;top:1855px">Data Platform<br>Project</div>
<div class="abs expert-label" style="left:770px;top:1855px">Training</div>
<div class="abs expert-label" style="left:947px;top:1855px">Cloud Solution<br>Provider</div>
<div class="abs strip">
  <div><i></i>Certifications</div>
  <div><i></i>Certified Cloud<br>Trainer</div>
  <div><svg width="40" height="34" viewBox="0 0 40 34"><rect x="2" y="8" width="36" height="24" rx="2" fill="none" stroke="#1ba7b0" stroke-width="2"/><path d="M14 8V3h12v5M2 18h36" fill="none" stroke="#1ba7b0" stroke-width="2"/></svg>Most Valuable<br>Professional</div>
  <div><i></i>Gold Partners</div>
</div>
<a class="abs btn" style="left:534px;top:2124px" href="#">Find Out More</a>
<div class="abs divider"></div>

<h2 class="abs section-title" style="left:111px;top:2274px">Latest News</h2>
<article class="abs news-card" style="left:111px" role="img" aria-label="Photo of a consultant at a laptop"><h4>New Gold certification obtained in July 2020</h4></article>
<article class="abs news-card" style="left:357px" role="img" aria-label="Photo of a consultant at a laptop"><h4>Evolution of the number of certification obtained by our consultants</h4></article>
<article class="abs news-card" style="left:604px" role="img" aria-label="Photo of a consultant at a laptop"><h4>Arrival of a new consultant / support function</h4></article>
<article class="abs news-card" style="left:850px" role="img" aria-label="Photo of a consultant at a laptop"><h4>Weekend / day / half-day between Brightvale. Show our cooperative side, cohesive team</h4></article>

<section class="abs testimonials">
  <div class="abs quote-card">
    <p>Lorem ipsum dolor sit amet, consectetur adipiscing elit, sed do eiusmod tempor incididunt ut labore et dolore magna aliqua. Ut enim ad minim veniam, quis nostrud exercitation ullamco laboris nisi ut aliquip ex ea commodo consequat.</p>
    <h4>Client Name</h4>
    <em>Position</em>
    <span class="abs quote-mark">”</span>
  </div>
  <div class="abs avatar" role="img" aria-label="Portrait of the client"></div>
  <div class="abs say">
    <h2>What they're saying about us</h2>
    <p>Lorem ipsum dolor sit amet, consectetur adipiscing elit, sed do eiusmod tempor incididunt ut labore et dolore magna aliqua.</p>
  </div>
  <div class="abs dots"><span></span><span></span><span></span><span></span></div>
  <div class="abs arrows">
    <svg width="26" height="14" viewBox="0 0 26 14"><path d="M25 7H2M8 1 2 7l6 6" fill="none" stroke="#1d2a2c" stroke-width="2"/></svg>
    <span style="width:1px;height:24px;background:#dfe4e5"></span>
    <svg width="26" height="14" viewBox="0 0 26 14"><path d="M1 7h23M18 1l6 6-6 6" fill="none" stroke="#1d2a2c" stroke-width="2"/></svg>
  </div>
</section>

<footer class="abs footer">
  <div class="abs foot-col" style="left:111px;width:220px;top:72px;color:var(--ink)">
    <p>Nemo enim ipsam voluptatem quia voluptas sit aspernatur aut odit aut fugit, sed quia consequuntur magni dolores eos qui ratione</p>
    <div class="socials"><span></span><span></span><span></span><span></span></div>
  </div>
  <div class="abs foot-col" style="left:446px;color:var(--muted)">
    <h4>Quick Links</h4>
    <ul><li>Home</li><li>Work</li><li>Capabilities</li><li>Squads</li><li>Get Started</li></ul>
  </div>
  <div class="abs foot-col" style="left:614px;width:220px;color:var(--ink)">
    <h4>Address</h4>
    <div class="contact-line" style="margin-top:14px"><svg width="10" height="13" viewBox="0 0 10 13"><path d="M5 0a5 5 0 0 1 5 5c0 3.5-5 8-5 8S0 8.5 0 5a5 5 0 0 1 5-5z" fill="#1ba7b0"/></svg><div><b>Brightvale Coop</b><br>18 Nemo enim ipsam volupt,<br>quia voluptas sit 6155</div></div>
    <div class="contact-line"><svg width="12" height="12" viewBox="0 0 12 12"><path d="M2 0h3l1 3-2 1.5a7 7 0 0 0 3.5 3.5L9 6l3 1v3a2 2 0 0 1-2 2A10 10 0 0 1 0 2a2 2 0 0 1 2-2z" fill="#1ba7b0"/></svg>+123-456-7890</div>
    <div class="contact-line"><svg width="13" height="10" viewBox="0 0 13 10"><rect width="13" height="10" fill="#1ba7b0"/><path d="m0 0 6.5 5L13 0" fill="none" stroke="#fff"/></svg>support@brightvale_coop.com</div>
  </div>
  <div class="abs foot-col newsletter" style="left:862px;width:230px;color:var(--text)">
    <h4>Subscribe Us</h4>
    <p style="margin-top:14px">Subscribe to my Newsletter! to get latest news and updates</p>
    <input type="text" placeholder="Your email Address">
    <button>SUBMIT</button>
  </div>
</footer>
<div class="abs copyright">Copyright 2019 © <b>Brightvale Coop</b> | Privacy Policy | Terms of Use | Design By Kestrel Webworks Inc.</div>

</body>
</html>
```